Need A Modern Website Design For ADSL2+ Provider

AIM: To sell affordable combined ADSL2+ Unlimited & phone line rentals to residential customers.

TYPE: This project is for DESIGN only (no code)

Source Files: I need all source files, fonts, images to be provided in ZIP format.

Logo: Existing (attached)

-Corporate Colours-
Black & Red (Same as Logo)
Others colours are fine as long as it looks corporate and modern.

-Pages-
Need another page to display our pricing plan

(1)Homepage Design
(2)Page to display our plans (needs to be in tables)
Example: http://lnkbrev.example/QwTr8k

-Pricing Plan-
(1) $59.95 / Month (Metro / City Areas)
(2) $79.95 / Month (Outside City Areas / Rural Areas)
Detailed Pricing plans is in PDF attached
Updates

Target Market(s)

Both male & female, Young & Old

Industry/Entity Type

Residential

Requirements
Must have
• + Graphic banner on the home page that shows our ADSL2+ combo plan for ADSL2+ Unlimited & Phone Line Rental for only $59.95

+ A box to allow customers to login to their account (username & password + login button)

+ Clearly display contact number
+ Button to sign up
+ Button to check service availability something like https://checkin.pelwara.example/wizard/

+ Button for Live Chat
+ Navigation menu
+ Social media icons Facenet, Google +, Chirper
+ Minimal text on homepage
+ Corporate & Friendly
Nice to have
• + Effective use of icons with corporate colours
+ Effective use of stockphotos
(use of people in photos would be nice)

+ Effective use of graphics to navigate people through the site and inform customers of specials,etc.
Should not have
• + Cluttered
+ Don’t want long scrolling homepage
+ Don’t want too much text on homepage 500 words is the estimate max.

```html
<!DOCTYPE html>
<html lang="en">
<head>
<meta charset="utf-8">
<title>ORBELL – Combo2+ Plans</title>
<link rel="stylesheet" href="https://fonts.googleapis.com/css2?family=Montserrat:wght@400;600&family=Ubuntu:wght@400;500;700&display=swap">
<style>
:root{
  --red:#c8141a;
  --red-dark:#9e0c10;
  --ink:#1d1d1f;
  --dark:#2a2c31;
  --darker:#1b1c1f;
  --paper:#efefef;
  --panel:#ffffff;
  --row-alt:#d9d9d9;
  --line:#b9b9b9;
  --muted:#555;
  --foot-text:#c9c9c9;
}
*{box-sizing:border-box;margin:0;padding:0}
html,body{width:840px;height:1200px;overflow:hidden}
body{background:var(--paper);font-family:"Ubuntu",sans-serif;color:var(--ink);position:relative}
.abs{position:absolute}

/* header */
.topbar{left:0;top:0;width:840px;height:50px;background:linear-gradient(#33363c,#24262a)}
.topbar-stripe{left:0;top:50px;width:840px;height:6px;background:linear-gradient(var(--red),var(--red-dark))}
.brand-tab{left:126px;top:0;width:174px;height:64px;background:linear-gradient(#fff,#dcdcdc);clip-path:polygon(0 0,100% 0,100% 88%,50% 100%,0 88%);display:flex;align-items:center;justify-content:center;gap:8px}
.brand-dot{width:22px;height:22px;border-radius:50%;background:var(--red)}
.brand-name{font-family:"Montserrat",sans-serif;font-weight:600;font-size:25px;color:var(--ink);letter-spacing:1px}
.nav{left:342px;top:17px;display:flex;gap:16px;font-size:8.6px;color:#d8d8d8}

/* hero */
.hero{left:0;top:56px;width:840px;height:240px;background:radial-gradient(ellipse at 55% 40%,#3b3e44,#222428 75%)}
.hero-base{left:0;top:294px;width:840px;height:8px;background:linear-gradient(#111,#3a3a3a)}
.hero-title{left:126px;top:100px;font-weight:700;font-size:21.5px;line-height:28.5px;color:#fff;text-shadow:2px 2px 0 var(--red-dark)}
.price-tag{background:var(--red);color:#fff;border:2px solid #fff;border-radius:9px;box-shadow:0 2px 4px rgba(0,0,0,.5)}
.price-tag.big{left:454px;top:140px;width:76px;height:50px;padding:3px 6px}
.price-tag.small{left:126px;top:222px;width:74px;height:50px;padding:3px 6px;background:#1f2023}
.price-amt{font-weight:700;font-size:27px;line-height:28px}
.price-amt sup{font-size:11px;vertical-align:top}
.price-per{position:absolute;right:6px;top:17px;font-size:8px;text-align:right;line-height:9px}
.price-note{font-size:7px;font-style:italic;margin-top:2px}
.hero-icon{top:229px;width:34px;height:33px;border:2px solid #fff;border-radius:4px;background:#2e3035;display:flex;align-items:center;justify-content:center}
.rental{font-size:8.5px;font-weight:700;font-style:italic;color:#fff;text-align:center;line-height:10px}
.plus{top:228px;color:#fff;font-size:28px;font-weight:700}
.photo-laptop{left:404px;top:222px;width:96px;height:72px;background:linear-gradient(140deg,#1a1a1a 40%,#6a8a4a 70%,#3a3a3a);border-radius:6px 6px 0 0}
.photo-presenter{left:532px;top:132px;width:180px;height:162px;background:linear-gradient(90deg,rgba(230,230,230,0) 0%,#d9d9d9 45%,#eeeeee 60%,rgba(220,220,220,0) 100%);border-radius:40% 40% 0 0}
.dots{left:405px;top:307px;display:flex;gap:3px}
.dots i{width:6px;height:6px;border-radius:50%;border:1px solid #bbb;background:#f6f6f6}
.dots i.on{background:var(--red);border-color:var(--red)}

/* action buttons */
.action{top:330px;width:181px;height:39px;background:linear-gradient(var(--red),var(--red-dark));box-shadow:0 2px 3px rgba(0,0,0,.3);color:#fff;display:flex;align-items:center;gap:8px;padding-left:8px}
.action-title{font-weight:500;font-size:13px;line-height:14px}
.action-sub{font-size:7.4px}
.chat-agent{width:26px;height:34px;align-self:flex-end;background:linear-gradient(#e9d3bf,#f4f4f4);border-radius:12px 12px 0 0}

/* plan panel */
.panel{left:126px;top:396px;width:588px;height:630px;background:var(--panel);box-shadow:0 0 3px rgba(0,0,0,.12)}
.plan-title{left:132px;top:405px;font-family:"Montserrat",sans-serif;font-size:19px;font-weight:400}
.plan-lead{left:132px;top:430px;font-family:"Montserrat",sans-serif;font-size:11px;color:#333}
.plans{left:132px;top:458px;width:570px;border-collapse:collapse;font-size:7px;color:#444;box-shadow:0 3px 4px rgba(0,0,0,.18)}
.plans th{height:35px;background:linear-gradient(#3a3a3a,#0c0c0c);color:#fff;font-weight:500;font-size:12.5px;line-height:12px;border-left:1px solid #555}
.plans th small{display:block;font-size:7px;font-weight:400;margin-top:1px}
.plans td{height:28px;padding:0 10px;border:1px solid var(--line);line-height:10px}
.plans tr:nth-child(even) td{background:var(--row-alt)}
.plans col.c1{width:198px}.plans col.c2{width:191px}.plans col.c3{width:181px}
.divider{left:138px;top:888px;width:564px;height:1px;background:#e2e2e2}

/* welcome + login */
.welcome-title{left:141px;top:907px;font-family:"Montserrat",sans-serif;font-size:12.5px}
.welcome-copy{left:142px;top:932px;width:370px;font-size:7.5px;line-height:11.5px;color:#222}
.welcome-copy p+p{margin-top:11px}
.login{left:538px;top:905px;width:158px;height:112px;border:1px solid #d2d2d2;background:#fff;box-shadow:0 1px 3px rgba(0,0,0,.2)}
.login-head{height:21px;background:linear-gradient(var(--red),var(--red-dark));color:#fff;font-size:12px;padding:3px 6px}
.login-field{margin:5px 0 0 6px;width:143px;height:15px;border:1px solid #ccc;background:#f4f4f4;font-size:7.5px;color:#555;padding:3px 6px}
.login-row{display:flex;justify-content:space-between;align-items:center;margin:5px 10px 0 6px}
.login-btn{width:40px;height:15px;background:linear-gradient(var(--red),var(--red-dark));color:#fff;font-size:7px;font-weight:700;text-align:center;line-height:15px;border-radius:2px}
.forgot{font-size:5.6px;color:var(--red)}

/* footer */
.footer{left:0;top:1039px;width:840px;height:137px;background:linear-gradient(#2c2e33,#24262a)}
.footer-col{top:1053px;color:var(--foot-text)}
.footer-col h3{font-weight:400;font-size:11px;color:#eee;margin-bottom:9px}
.footer-col li{list-style:none;font-size:7.4px;line-height:13.8px}
.footer-col h3.sub{margin:8px 0 6px}
.footer-rule{top:1054px;width:1px;height:110px;background:#3a3c41}
.social{display:flex;align-items:center;gap:8px;height:17px;margin-bottom:7px;font-size:7.6px}
.social i{width:14px;height:14px;background:#3b73b9;display:inline-block;border-radius:2px}
.copyright{left:0;top:1176px;width:840px;height:24px;background:#141517;color:#ddd;font-size:6.6px;padding:8px 146px}
</style>
</head>
<body>

<div class="abs topbar"></div>
<div class="abs topbar-stripe"></div>
<div class="abs brand-tab"><span class="brand-dot"></span><span class="brand-name">ORBELL</span></div>
<nav class="abs nav"><span>Home</span><span>Residential</span><span>Business</span><span>Member Services</span><span>News</span><span>Special Offers</span><span>Contact Us</span></nav>

<section class="abs hero"></section>
<div class="abs hero-base"></div>
<h1 class="abs hero-title">UNLIMITED ADSL2+<br>COMBO PLAN FOR ADSL2 &amp;<br>PHONE LINE RENTAL FOR ONLY</h1>
<div class="abs price-tag big"><div class="price-amt"><sup>$</sup>59<sup>.95</sup></div><div class="price-per"><br>P/M</div><div class="price-note">Lorem ipsum dolor</div></div>
<div class="abs photo-presenter" role="img" aria-label="Smiling businessman in white shirt and tie presenting the offer"></div>

<div class="abs price-tag small"><div class="price-amt"><sup>$</sup>59<sup>.95</sup></div><div class="price-per"><br>P/M</div><div class="price-note">Lorem ipsum dolor</div></div>
<div class="abs hero-icon" style="left:219px">
  <svg width="24" height="24" viewBox="0 0 24 24" fill="none" stroke="#fff" stroke-width="1.6"><circle cx="11" cy="11" r="9"/><ellipse cx="11" cy="11" rx="4" ry="9"/><path d="M2 11h18M4 6h14M4 16h14"/><path d="M14 13l7 3-3 1-1 3z" fill="#fff"/></svg>
</div>
<div class="abs plus" style="left:259px">+</div>
<div class="abs hero-icon" style="left:282px">
  <svg width="24" height="22" viewBox="0 0 24 22" fill="#fff"><path d="M2 7c0-3 4-5 10-5s10 2 10 5v2h-5V7H7v2H2z"/><path d="M5 11h14l2 9H3z"/><circle cx="12" cy="15" r="3" fill="#2e3035"/></svg>
</div>
<div class="abs plus" style="left:322px">+</div>
<div class="abs hero-icon" style="left:345px"><span class="rental">Line<br>Rental</span></div>
<div class="abs plus" style="left:386px">+</div>
<div class="abs photo-laptop" role="img" aria-label="Young woman smiling behind an open laptop"></div>
<div class="abs dots"><i></i><i class="on"></i><i></i><i></i></div>

<a class="abs action" style="left:126px">
  <svg width="34" height="28" viewBox="0 0 34 28" fill="none" stroke="#fff" stroke-width="2.6"><path d="M8 24a7 7 0 0 1 1-14 9 9 0 0 1 17 2 6 6 0 0 1 1 12z"/><path d="M11 15l5 5 9-10"/></svg>
  <div><div class="action-title">Check Service</div><div class="action-sub">Lorem ipsum dolor sit amet consec...</div></div>
</a>
<a class="abs action" style="left:329px">
  <svg width="36" height="28" viewBox="0 0 36 28" fill="#fff"><circle cx="12" cy="8" r="5"/><path d="M2 24c0-6 4-10 10-10s10 4 10 10z"/><circle cx="26" cy="20" r="7"/><path d="M26 16v8M22 20h8" stroke="var(--red)" stroke-width="2"/></svg>
  <div><div class="action-title">Sign Up</div><div class="action-sub">Lorem ipsum dolor sit amet consec...</div></div>
</a>
<a class="abs action" style="left:533px">
  <div class="chat-agent" role="img" aria-label="Support agent wearing a headset"></div>
  <div><div class="action-title">Live Chat</div><div class="action-sub">Lorem ipsum dolor sit amet consec...</div></div>
</a>

<main class="abs panel"></main>
<h2 class="abs plan-title">ORBELL Combo2+</h2>
<p class="abs plan-lead">Combo2+ offers line rental with Unlimited ADSL2+ Broadband.</p>

<table class="abs plans">
  <colgroup><col class="c1"><col class="c2"><col class="c3"></colgroup>
  <thead>
    <tr><th>Combo2+ plans<small>Effective 1 january 2013</small></th><th>Metro<small>On Net</small></th><th>Regional Off Net<small>(It Metro on-net not available)</small></th></tr>
  </thead>
  <tbody>
    <tr><td>Minimum Monthly Charge, including line rental and Unlimited ADSL2+</td><td>$59.95</td><td>$79.95</td></tr>
    <tr><td>Local Calls</td><td>18cents/call</td><td>18cents/call</td></tr>
    <tr><td>National Long Distance Calls (per Minute)<br>Plus Cap National Long Distance Calls</td><td>29cents $1.89 for first 20 minutes then per minute rate applies</td><td>29cents $1.89 for first 20 minutes then per minute rate applies</td></tr>
    <tr><td>Calls to Mobiles within Australia (per Minute)<br>Plus Cap Calls to mobile</td><td>35cents $3.40 for the first 20 minutes then per minute rate appliess</td><td>35cents $3.40 for the first 20 minutes then per minute rate appliess</td></tr>
    <tr><td>13/1300 Calls per call</td><td>44cents</td><td>44cents</td></tr>
    <tr><td>International calls</td><td>Refer standard rates sheet</td><td>Refer standard rates sheet</td></tr>
    <tr><td>Call Connection Fee (timed calls)</td><td>39 cents per call</td><td>39 cents per call</td></tr>
    <tr><td>Minimun 24 month contract cost including Delivery and Handling fee for the WIFI modem</td><td>$1,463.75</td><td>$1,943.75</td></tr>
    <tr><td>WIFI Modem (included in cost)</td><td>No Charge</td><td>No Charge</td></tr>
    <tr><td>Delivery and Handling fee of Modem</td><td>One off charge of $24.95</td><td>One off charge of $24.95</td></tr>
    <tr><td>Set up fee</td><td>No Charge</td><td>No Charge</td></tr>
    <tr><td>Termination fee</td><td>$250 if any part of service is cancelled or transferred before the end of the 24 month term</td><td>$250 if any part of service is cancelled or transferred before the end of the 24 month term</td></tr>
    <tr><td>Administration fee (per month)</td><td>$10 administration fee if pre selected to other service Provider</td><td>$10 administration fee if pre selected to other service Provider</td></tr>
  </tbody>
</table>

<div class="abs divider"></div>
<h2 class="abs welcome-title">Welcome to ORBELL</h2>
<div class="abs welcome-copy">
  <p>Le Lorem Ipsum est simplement du faux texte employé dans la composition et la mise en page avant impression. Le Lorem Ipsum est le faux texte standard de l'imprimerie depuis les années 1500.</p>
  <p>Quand un peintre anonyme assembla ensemble des morceaux de texte pour réaliser un livre spécimen de polices de texte. Il n'a pas fait que survivre cinq siècles, mais s'est aussi adapté à la bureautique informatique, sans que son contenu n'en soit modifiéuand un peintre anonyme assembla ensemble des morceaux de texte pour réaliser un livre spécimen de</p>
</div>

<aside class="abs login">
  <div class="login-head">Account Login</div>
  <div class="login-field">Account</div>
  <div class="login-field">Username</div>
  <div class="login-field">•••••••••</div>
  <div class="login-row"><span class="login-btn">Login</span><span class="forgot">Forgot Password</span></div>
</aside>

<footer class="abs footer"></footer>
<div class="abs footer-col" style="left:146px"><h3>About Orbell</h3><ul><li>CRM</li><li>Analytics</li><li>Automation</li><li>Reselling</li><li>Editions</li><li>Testimonials</li></ul></div>
<div class="abs footer-rule" style="left:284px"></div>
<div class="abs footer-col" style="left:320px"><h3>About Us</h3><ul><li>Schedule A Demo</li><li>Contact Us</li><li>Who We Are</li><li>Case Studies</li><li>Our SEO Side</li></ul></div>
<div class="abs footer-rule" style="left:422px"></div>
<div class="abs footer-col" style="left:462px"><h3>Support</h3><ul><li>Support Community</li><li>Getting Started Guide</li></ul><h3 class="sub">Video</h3><ul><li>Quick Video Orbell Services</li></ul></div>
<div class="abs footer-rule" style="left:594px"></div>
<div class="abs footer-col" style="left:626px"><h3>Social Media</h3>
  <div class="social">Facenet <i style="margin-left:6px"></i></div>
  <div class="social">Chirper <i style="margin-left:9px"></i></div>
</div>
<div class="abs copyright">Copyright © 2013 Orbell Pty Ltd. All Rights Reserved.</div>

</body>
</html>
```